Thai Restaurant Billboard Design

Design a billboard promoting food delivery during this Coronavirus time. We want to grab attention by embracing the Coronavirus and offering food delivery. People are sitting at home and this is the right time to promote food delivery.

I have the logo and spec sheet attached.

Target Market(s)

Anyone.

Requirements
Must have
• Top Heading should be big and bold:

Coronavirus Got You Quarantined?

Then put under

We Deliver
Healthy Thai Food!
Put the logo that is attached
415-283-6071
Nice to have
• Eyecatching. Creative.
Should not have
• Don't have any not haves. Make it look good.

```html
<!DOCTYPE html>
<html lang="en">
<head>
<meta charset="utf-8">
<title>Siam Lotus Kitchen – Delivery Billboard</title>
<link rel="stylesheet" href="https://fonts.googleapis.com/css2?family=Montserrat:wght@400;500;700;800&display=swap">
<style>
  :root {
    --page-bg: #e9ecef;
    --board-bg: #0b0b0c;
    --ink-white: #ffffff;
    --accent-yellow: #ffcc00;
    --ink-dark: #141414;
    --photo-deep: #1c1a19;
    --photo-mid: #4a3a2a;
    --photo-warm: #8a6a44;
  }
  * { margin: 0; padding: 0; box-sizing: border-box; }
  html, body {
    width: 1200px;
    height: 780px;
    overflow: hidden;
    background: var(--page-bg);
    font-family: "Montserrat", sans-serif;
  }
  .billboard {
    position: absolute;
    left: 0;
    top: 184px;
    width: 1200px;
    height: 412px;
    background: var(--board-bg);
    overflow: hidden;
  }
  .food-photo {
    position: absolute;
    left: 0;
    top: 0;
    width: 620px;
    height: 412px;
    background:
      radial-gradient(circle at 160px 280px, var(--photo-warm) 0, var(--photo-mid) 70px, var(--photo-deep) 170px, transparent 200px),
      linear-gradient(150deg, var(--photo-mid) 0%, #2a221b 30%, transparent 62%);
    clip-path: polygon(0 50px, 60px 50px, 620px 412px, 0 412px);
  }
  .headline-main {
    position: absolute;
    left: 210px;
    top: 18px;
    font-size: 112px;
    font-weight: 800;
    line-height: 1;
    letter-spacing: -1px;
    color: var(--ink-white);
  }
  .headline-sub {
    position: absolute;
    left: 455px;
    top: 118px;
    white-space: nowrap;
    line-height: 1;
  }
  .headline-sub .got-you {
    font-size: 41px;
    font-weight: 800;
    color: var(--ink-white);
    margin-right: 14px;
    vertical-align: 14px;
  }
  .headline-sub .quarantined {
    font-size: 72px;
    font-weight: 800;
    color: var(--accent-yellow);
    letter-spacing: -0.5px;
  }
  .burst {
    position: absolute;
    stroke: var(--accent-yellow);
    stroke-width: 2.5;
    stroke-linecap: round;
    fill: none;
  }
  .burst-top { left: 910px; top: 8px; }
  .burst-left { left: 392px; top: 140px; }
  .brand-name {
    position: absolute;
    left: 462px;
    top: 300px;
    width: 200px;
    text-align: center;
    font-size: 20px;
    font-weight: 700;
    color: var(--ink-white);
    line-height: 1.2;
  }
  .brand-name::before {
    content: "";
    display: block;
    width: 40px;
    height: 40px;
    margin: 0 auto 12px;
    background: var(--ink-white);
  }
  .offer-band {
    position: absolute;
    left: 667px;
    top: 243px;
    width: 485px;
    height: 51px;
    background: var(--accent-yellow);
    color: var(--ink-dark);
    display: flex;
    align-items: center;
    justify-content: center;
    font-size: 25px;
    white-space: nowrap;
  }
  .offer-band .offer-lead { font-weight: 500; margin-right: 12px; }
  .offer-band .offer-strong { font-weight: 800; }
  .phone-number {
    position: absolute;
    left: 680px;
    top: 304px;
    font-size: 66px;
    font-weight: 500;
    letter-spacing: 3px;
    color: var(--ink-white);
    line-height: 1.2;
  }
</style>
</head>
<body>
  <main class="billboard">
    <div class="food-photo" role="img" aria-label="Plate of shrimp pad thai with lime and green onion on a bamboo mat"></div>

    <h1 class="headline-main">Coronavirus</h1>
    <svg class="burst burst-top" width="70" height="70" viewBox="0 0 70 70" aria-hidden="true">
      <line x1="10" y1="40" x2="36" y2="6"/>
      <line x1="14" y1="50" x2="38" y2="36"/>
      <line x1="18" y1="62" x2="60" y2="62"/>
    </svg>
    <h2 class="headline-sub"><span class="got-you">Got You</span><span class="quarantined">Quarantined?</span></h2>
    <svg class="burst burst-left" width="60" height="64" viewBox="0 0 60 64" aria-hidden="true">
      <line x1="4" y1="10" x2="46" y2="10"/>
      <line x1="20" y1="32" x2="48" y2="20"/>
      <line x1="28" y1="58" x2="50" y2="28"/>
    </svg>

    <div class="brand-name">Siam Lotus Kitchen</div>

    <p class="offer-band"><span class="offer-lead">We Deliver</span><span class="offer-strong">Healthy Thai Food!</span></p>
    <p class="phone-number">415-283-6071</p>
  </main>
</body>
</html>
```